Flat bootstrap design for existing site

I'm looking for a modern flat design based around an existing logo. This has to be a custom design (no external templates), and implemented into a bootstrap framework.

The logo is attached as 2 versions - choose whichever you want, that flows better with whatever design you choose.

Added screenshots of the existing site (currently using the default bootstrap layouts). Please make your designs around those pages in the screenshots (i.e. the homepage only has the postal code input and the header). The active page has 3 screenshots, because I wanted to illustrate the other states that would be visible (in the table rows).

This is a moving/junk removal website, just for some context.

Here's some example websites (flat designs) that I like, just to give you an idea of what I'm after.

https://www.plivoterra.com/
https://damsoqua.com/
https://trevalin.com/
https://morkadelphi.com/en/

Coding

Coded - Design and coding required

Number of Pages Required

5+ page

Colors

Designer to choose colors to be used in the design.

Requirements
Must have
• It must be a modern/simple flat design, that is built around the existing logo (attached).
• It has to be implemented using bootstrap.

```html
<!DOCTYPE html>
<html lang="en">
<head>
<meta charset="utf-8">
<title>HAULIX – Book</title>
<link rel="stylesheet" href="https://fonts.googleapis.com/css2?family=Lato:wght@400;700;900&display=swap">
<style>
:root{
  --brand:#35c9f7;
  --brand-soft:#62d5f9;
  --row-light:#c5effc;
  --row-mid:#a5e6fb;
  --row-line:#4ecbf1;
  --accent:#f7951d;
  --ink:#2b2f33;
  --muted:#7c868c;
  --notice:#93dcf6;
  --white:#ffffff;
}
*{box-sizing:border-box;margin:0;padding:0}
html,body{width:1200px;height:778px;overflow:hidden;background:var(--white);font-family:"Lato",sans-serif;color:var(--ink)}
.page{position:relative;width:1200px;height:778px}
.topbar{position:absolute;left:0;top:0;width:1200px;height:67px;background:var(--brand)}
.brand{position:absolute;left:80px;top:0;width:176px;height:67px;background:var(--brand-soft);display:flex;align-items:center;justify-content:center;gap:8px;color:var(--white);font-weight:900;font-size:30px;letter-spacing:1px}
.brand-dot{width:12px;height:12px;border-radius:50%;background:var(--white)}
.nav{position:absolute;top:0;height:67px;display:flex;align-items:center;color:var(--white);font-weight:700;font-size:15px}
.nav-book{left:589px;top:18px;height:31px;width:69px;justify-content:center;border:2px solid var(--white)}
.nav-how{left:680px}
.nav-driver{left:834px}
.nav-user{left:1002px;font-size:14px}
.caret{margin-left:6px;width:0;height:0;border-left:5px solid transparent;border-right:5px solid transparent;border-top:6px solid var(--accent)}
.cursor{position:absolute;left:648px;top:40px}
.section-title{position:absolute;left:94px;color:var(--brand);font-weight:700;font-size:20px;line-height:24px;letter-spacing:.2px}
.panel{position:absolute;left:91px;width:1019px;background:var(--brand)}
.booking{top:121px;height:210px}
.field-label{position:absolute;font-size:18px;line-height:22px;color:var(--ink)}
.field{position:absolute;background:var(--white);border-radius:3px;font-size:18px;line-height:22px;display:flex;align-items:center;padding-left:31px}
.field svg{position:absolute;right:16px}
.field-desc{align-items:flex-start;padding-top:8px;padding-left:40px}
.btn-update{position:absolute;left:524px;top:152px;width:146px;height:49px;background:var(--accent);color:var(--white);font-weight:700;font-size:19px;display:flex;align-items:center;justify-content:center;border-radius:2px}
.spinner{position:absolute;left:526px;top:355px}
.notice{position:absolute;left:601px;top:386px;width:508px;height:34px;background:var(--notice);color:var(--muted);font-size:17px;display:flex;align-items:center;padding-left:17px;border-radius:2px}
.drivers{top:424px;height:331px}
.drivers-inner{position:absolute;left:20px;top:16px;width:977px;height:297px;background:var(--white)}
.table{position:absolute;left:28px;top:20px;width:923px}
.row{position:relative;height:52px;font-size:18px}
.row.head{height:45px;color:var(--muted)}
.row.light{background:var(--row-light)}
.row.mid{background:var(--row-mid)}
.row+.row.mid,.row.light+.row.light,.row.mid+.row.light{border-top:3px solid var(--row-line)}
.cell{position:absolute;top:50%;transform:translateY(-50%);white-space:nowrap}
.c-name{left:19px}.c-dist{left:219px}.c-time{left:380px}.c-status{left:582px}.c-pay{left:742px}
.btn-pay{position:absolute;left:747px;top:11px;width:166px;height:31px;background:var(--accent);color:var(--white);font-size:18px;display:flex;align-items:center;justify-content:center}
</style>
</head>
<body>
<div class="page">
  <header class="topbar">
    <div class="brand"><span class="brand-dot"></span>HAULIX</div>
    <div class="nav nav-book">BOOK</div>
    <div class="nav nav-how">HOW IT WORKS</div>
    <div class="nav nav-driver">BECOME A DRIVER</div>
    <div class="nav nav-user">georgia@postvale<span class="caret"></span></div>
    <svg class="cursor" width="26" height="26" viewBox="0 0 26 26"><path d="M2 2 L2 20 L7 15 L11 23 L14 21 L10 14 L17 14 Z" fill="#fff" stroke="#35c9f7" stroke-width="1"/></svg>
  </header>

  <h2 class="section-title" style="top:92px">BOOKING DETAILS</h2>
  <section class="panel booking">
    <div class="field-label" style="left:76px;top:9px">Package selected</div>
    <div class="field" style="left:76px;top:37px;width:422px;height:58px">Package 1
      <svg width="16" height="13" viewBox="0 0 16 13"><path d="M0 0H16L8 13Z" fill="#35c9f7"/></svg>
    </div>
    <div class="field-label" style="left:76px;top:117px">Pick-up time selected</div>
    <div class="field" style="left:76px;top:143px;width:422px;height:58px">July 18 @ 4:15 pm
      <svg width="24" height="24" viewBox="0 0 24 24"><circle cx="12" cy="12" r="10" fill="none" stroke="#35c9f7" stroke-width="1.6"/><path d="M12 6V12H17" fill="none" stroke="#35c9f7" stroke-width="1.6"/></svg>
    </div>
    <div class="field-label" style="left:524px;top:9px">Description</div>
    <div class="field field-desc" style="left:524px;top:37px;width:420px;height:99px">1 gas stove</div>
    <div class="btn-update">UPDATE</div>
  </section>

  <svg class="spinner" width="60" height="70" viewBox="0 0 60 70">
    <circle cx="33" cy="14" r="9" fill="#35c9f7"/>
    <circle cx="18" cy="20" r="7" fill="#35c9f7"/>
    <circle cx="10" cy="34" r="6" fill="#35c9f7"/>
    <circle cx="16" cy="48" r="5" fill="#35c9f7"/>
    <circle cx="30" cy="53" r="4" fill="#35c9f7"/>
    <circle cx="42" cy="46" r="3" fill="#35c9f7"/>
    <circle cx="47" cy="35" r="2" fill="#35c9f7"/>
    <circle cx="46" cy="23" r="1.3" fill="#35c9f7"/>
  </svg>
  <div class="notice">Please stay on this page while we process your request.</div>

  <h2 class="section-title" style="top:396px">DRIVERS IN YOUR AREA</h2>
  <section class="panel drivers">
    <div class="drivers-inner">
      <div class="table">
        <div class="row head"><span class="cell c-name">Name</span><span class="cell c-dist">Distance (km)</span><span class="cell c-time">Pick-up Time</span><span class="cell c-status">Status</span><span class="cell c-pay">Payment</span></div>
        <div class="row light"><span class="cell c-name">Perry Stroud</span><span class="cell c-dist">4.4 km</span><span class="cell c-time">July 18 @ 4:15pm</span><span class="cell c-status">Accepted</span><span class="btn-pay">Make Payment</span></div>
        <div class="row mid"><span class="cell c-name">Tobias Crane</span><span class="cell c-dist">5.4 km</span><span class="cell c-status">Pending</span></div>
        <div class="row light"><span class="cell c-name">Edmund Ulrey</span><span class="cell c-dist">10.4 km</span><span class="cell c-status">Pending</span></div>
        <div class="row mid"><span class="cell c-name">Victor Jansen</span><span class="cell c-dist">10.9 km</span><span class="cell c-status">Pending</span></div>
      </div>
    </div>
  </section>
</div>
</body>
</html>
```